Modern and Clean Web Re-Design Project

We have 2 companies in similar industries: Printing and Mail Preparation/Fulfillment. We prefer sites that are clean and easy to navigate.Our printing company, Harbourline Press Works' website, hpwdirect.example is outdated needs revamping. We have rebranded our logo and are looking for a new design that is clean, modern and geared to other corporations and business in the downtown Toronto area. Our mailing company, The Postwick Depot (thepostwickdepot.example) needs a website as well. This company is in the Direct Mail and letter shop business, which essentially is addressing/personalizing people's printed matter and preparing it for either the Canadian or US postal service. The Postwick Depot specializes in not-for-profit and corporate sectors.Please see our logos to get an idea of the colors and look we want. For all intensive purposes, the sites can look similar in design all we want is that each site has the appropriate corporate colors and is a bit different so they don't look identical as the two business run as separate corporations.The content of the website should be easily changed by our staff and we want it to be setup to optimized for SEO based on the keywords we want. We are looking for someone to work on this project immediately
Updates

Project Deadline Extended
Reason: Change of ideas

After doing some thinking, I would like the site to be more modern but the non flash sites that I have seen so far Im finding life-less and while I want something clean, not overly busy and corporate looking, I dont want the design to be bland looking.

Please design with the previous specs in mind but with a twist as mentioned above.

Thanks
Dorian

Target Market(s)

See above

Industry/Entity Type

Printing

Requirements
Must have
• Must match the design and style of each respective logoSee the attached impage of the front of our offices to have an idea of our lookWe must be able to edit the content ourselves without any fancy programs or tools.Must be SEO optimized
Nice to have
• An online order form that can be emailed to us for quotes.....perhaps a page with a bunch of fields that have drop down menus....
Should not have
• Should not be overly busy. I want it to be clean and simple but informative without being hard to navigate

```html
<!DOCTYPE html>
<html lang="en">
<head>
<meta charset="utf-8">
<title>Harbourline Press Works</title>
<link rel="stylesheet" href="https://fonts.googleapis.com/css2?family=Roboto+Condensed:wght@400;700&family=Arimo:wght@400;700&display=swap">
<style>
:root{
  --orange:#fe9a35;
  --brand-red:#c9431f;
  --band-top:#b53a13;
  --band-bottom:#d3582c;
  --ink:#222;
  --body:#4a4a4a;
  --heading:#555;
  --rule:#dcdcdc;
  --page:#f4f4f4;
  --footer:#0a0a0a;
}
*{box-sizing:border-box;margin:0;padding:0}
html,body{width:1083px;height:1200px;overflow:hidden}
body{position:relative;background:var(--page);font-family:"Arimo",Arial,sans-serif;color:var(--body)}
.site-header{position:absolute;left:0;top:0;width:1083px;height:106px;background:linear-gradient(#fbfbfb,#e9e9e9)}
.brand{position:absolute;left:108px;top:30px;font-family:"Roboto Condensed",sans-serif;font-weight:700;font-size:27px;color:var(--brand-red);display:flex;align-items:center;gap:10px}
.brand-dot{width:22px;height:22px;border-radius:50%;background:var(--orange)}
.call{position:absolute;right:108px;top:38px;font-family:"Roboto Condensed",sans-serif;font-size:22px;color:var(--brand-red)}
.main-nav{position:absolute;left:0;top:106px;width:1083px;height:46px;background:var(--orange)}
.main-nav ul{list-style:none;position:relative;height:100%}
.main-nav li{position:absolute;top:14px;font-family:"Roboto Condensed",sans-serif;font-size:15px;color:#fff}
.hero-band{position:absolute;left:0;top:152px;width:1083px;height:403px;background:linear-gradient(var(--band-top),var(--band-bottom))}
.hero{position:absolute;left:107px;top:27px;width:868px;height:345px;border:1px solid #e7b8a4;background:linear-gradient(110deg,#3f6e8c 0%,#e9a23a 30%,#7a2a4a 55%,#e05a7d 75%,#f0c23a 100%);box-shadow:0 10px 10px -6px rgba(0,0,0,.35)}
.hero-copy{position:absolute;left:419px;top:106px;width:440px;font-family:"Roboto Condensed",sans-serif;font-size:25px;line-height:32px;color:#fff;text-shadow:0 1px 2px rgba(0,0,0,.4)}
.pager{position:absolute;left:378px;bottom:0;width:113px;height:24px;border-radius:6px 6px 0 0;background:#d9d9d9;display:flex;gap:6px;justify-content:center;align-items:center}
.pager span{width:11px;height:11px;border-radius:50%;background:#8b8b8b}
.pager span.on{background:#e08a36}
.work-grid{position:absolute;top:578px;left:107px;width:868px;height:119px}
.work-item{position:absolute;top:0;width:199px;height:119px}
.col{position:absolute;top:744px;width:271px}
.col h2{font-family:"Roboto Condensed",sans-serif;font-weight:400;font-size:21px;color:var(--heading);padding-bottom:8px;border-bottom:1px solid var(--rule);margin-bottom:12px}
.col .lead{font-weight:700;color:var(--ink);font-size:10.5px;line-height:14.5px;margin-bottom:14px}
.col p{font-size:10.5px;line-height:14.5px;margin-bottom:14px}
.news-head{display:flex;justify-content:space-between;align-items:center}
.view{font-family:"Arimo",sans-serif;font-weight:700;font-size:11px;color:var(--ink);border-left:1px solid var(--rule);padding:2px 0 2px 13px;display:flex;align-items:center;gap:10px}
.view i{width:0;height:0;border-left:6px solid #f0a020;border-top:4px solid transparent;border-bottom:4px solid transparent}
.news-item{font-size:10.5px;line-height:13.5px;padding-bottom:9px;margin-bottom:9px;border-bottom:1px solid var(--rule)}
.news-item:last-child{border-bottom:0}
.news-item b{color:var(--brand-red)}
.clients{position:absolute;left:107px;top:1032px;width:868px;height:85px;border:1px solid #ddd;background:#f1f1f1}
.clients ul{list-style:none;position:absolute;left:15px;top:27px;width:836px;height:33px;background:#fff;display:flex;justify-content:space-around;align-items:center}
.clients li{font-family:"Roboto Condensed",sans-serif;font-weight:700;font-size:19px;color:#3a3a3a}
.site-footer{position:absolute;left:0;top:1144px;width:1083px;height:56px;background:var(--footer)}
.copyright{position:absolute;left:117px;top:22px;font-size:10.5px;color:#a8a8a8}
.social{position:absolute;left:824px;top:17px;display:flex;gap:8px;list-style:none}
.social li{width:23px;height:23px;background:#5a5a5a;border-radius:2px}
</style>
</head>
<body>
<header class="site-header">
  <div class="brand"><span class="brand-dot"></span>Harbourline Press Works</div>
  <div class="call">CALL US: 416 555 0147</div>
</header>
<nav class="main-nav">
  <ul>
    <li style="left:126px">HOME</li>
    <li style="left:214px">WHO WE ARE</li>
    <li style="left:345px">WHAT WE DO</li>
    <li style="left:479px">SERVICES</li>
    <li style="left:594px">PORTFOLIO</li>
    <li style="left:719px">TESTIMONIALS</li>
    <li style="left:871px">CONTACT US</li>
  </ul>
</nav>
<section class="hero-band">
  <div class="hero" role="img" aria-label="Colourful feathers with cyan, magenta, yellow and black paint drops">
    <p class="hero-copy">perspiciatis unde omnis iste natus error sit voluptatem accusantium doloremque lau-dantium, torm rem aperiam</p>
    <div class="pager"><span></span><span></span><span class="on"></span><span></span><span></span><span></span></div>
  </div>
</section>
<section class="work-grid">
  <div class="work-item" style="left:0;background:linear-gradient(#2a2a2a,#5a4a42)" role="img" aria-label="Office storefront at night"></div>
  <div class="work-item" style="left:223px;background:linear-gradient(135deg,#e9e6e2,#f0a23a 50%,#dcd8d2)" role="img" aria-label="Branding print sample with orange cubes"></div>
  <div class="work-item" style="left:446px;background:linear-gradient(90deg,#f2f2f2,#e8e2dc 55%,#1fa0a0)" role="img" aria-label="Printed brochure with children at a table"></div>
  <div class="work-item" style="left:669px;background:linear-gradient(135deg,#111 20%,#f08a1c 40%,#f0901e 80%,#111)" role="img" aria-label="Orange folded event card"></div>
</section>
<section class="col" style="left:108px">
  <h2>Who we are</h2>
  <p class="lead">mpora incidunt ut labore et dolore magnam aliquam quaerat voluptatem. Ut enim ad minima ven quis nostrum exercitationem ullam corporis suscipit laboriosam,</p>
  <p>Sed ut perspiciatis unde omnis iste natus error sit volup-tatem accusantium doloremque laudantium, torm rem aperiam, eaque ipsa quae ab illo inventore veritatis et quasi architecto beatae vitae dicta sunt explicabo. Nemo sam voluptatem quia voluptas sit aspernatur aut odit aut fugit, sed quia consequuntur magni dolores eos ectetur,</p>
  <p>adipisci velit, sed quia nnumquam eius modi tempora incidunt ut labore et dolore magnam aliquam quaerat</p>
</section>
<section class="col" style="left:407px">
  <h2>What We Do ?</h2>
  <p class="lead">mpora incidunt ut labore et dolore magnam aliquam quaerat voluptatem. Ut enim ad minima ven quis nostrum exercitationem ullam corporis suscipit laboriosam,</p>
  <p>Sed ut perspiciatis unde omnis iste natus error sit volup-tatem accusantium doloremque laudantium, torm rem aperiam, eaque ipsa quae ab illo inventore veritatis et quasi architecto beatae vitae dicta sunt explicabo. Nemo sam voluptatem quia voluptas sit aspernatur aut odit aut fugit, sed quia consequuntur magni dolores eos qui ratione voil sequi nesciunt. ,</p>
  <p>adipisci velit, sed quia nnumquam eius modi tempora incidunt ut labore et dolore magnam aliquam quaerat</p>
</section>
<section class="col" style="left:707px">
  <h2 class="news-head">Latest news <span class="view">VIEW <i></i></span></h2>
  <div class="news-item"><b>"Lorem ipsum dolor sit amet, consectetur</b> adipisicing elit, sed do eiusmod tempor incididunt ut labore et dolore magna aliqua. Ut enim ad minim veniam, quis nostrud exercitation ullamco laboris nisi ut"</div>
  <div class="news-item"><b>"Lorem ipsum dolor sit amet, consectetur</b> adipisicing elit, sed do eiusmod tempor incididunt ut labore et dolore magna aliqua. Ut enim ad minim veniam, quis nostrud exercitation ullamco laboris nisi ut"</div>
  <div class="news-item"><b>"Lorem ipsum dolor sit amet, consectetur</b> adipisicing elit, sed do eiusmod tempor incididunt ut labore et dolore magna aliqua. Ut enim ad minim veniam, quis nostrud exercitation ullamco laboris nisi ut"</div>
</section>
<section class="clients">
  <ul>
    <li>Norvell</li><li>Castrim</li><li>Velmora</li><li>Pendrick</li><li>Halvane</li><li>Riverline</li><li>Quenfield</li>
  </ul>
</section>
<footer class="site-footer">
  <p class="copyright">© 2012 HPW Direct. All rights reserved.</p>
  <ul class="social" aria-label="Social links">
    <li></li><li></li><li></li><li></li><li></li>
  </ul>
</footer>
</body>
</html>
```